postcard design for a design company to promote itself in a new area

I am putting out postcards to hairdressing salons that I have renovated recently to target there client base and to offer a discount to the initial consult to there loyal clients. I would like to have a vibrant front design that I can change every twelve weeks with my logo (existing) imbedding into a vibrate, energetic, stylish yet creative front. I want something very colourful fun and inviting that makes people want to pick it up, it should contain some style of pattern and I don't want it all to be my logo. My existing logo I would like on the front but only small or built into the pattern it can be in a different colour and the out side shape can change as long its still the same letters etc.. The pattern can contain words.. The following is what I have written that will be on the back of the post card so you can understand the feel of it.

Marlie from Kestrel Interiors is partnering up with Bellora and Gwenda from Pim Locks
As we have something special in common, we both want our clients to look & feel fabulous
Marlie is offering the loyal clients of Pim Locks a special in home consult at a reduced rate.
What we do: Create innovative yet practical design solutions, window treatments & furniture, which are stylish, happy & memorable. Design to us is about you, who you are & how you live, we are passionate about creating a space that is for you and about you.
A well-designed space makes you feel 10 years younger and truly fabulous to be in, it does not have to cost the earth, but it is something everyone should go home to…
Call today to find out how we can add value & create a space that makes you feel wonderful to be in.
m 0413 925 716

Any suggestions on the wording would be appreciated... Especially the 'A well designed space makes you feel 10years younger'

I have attached my existing logo the colour can change.

I want to reach out to the people sitting in the chair getting there hair done and make them want to know a little more about my business. I would like the post card to feel fresh young new and happy.

```html
<!DOCTYPE html>
<html lang="en">
<head>
<meta charset="utf-8">
<title>Kestrel Interiors – Postcard</title>
<link href="https://fonts.googleapis.com/css2?family=Roboto+Condensed:wght@400;700&family=Montserrat:wght@500&display=swap" rel="stylesheet">
<style>
  :root {
    --page-bg: #ebe7e4;
    --frame: #4a4646;
    --ink: #2e2a2b;
    --ink-soft: #4d4748;
    --logo-disc: #3d3537;
    --white: #ffffff;
    --magenta: #c81f9a;
    --hot-pink: #e8329a;
    --rose: #e98fbf;
    --lavender: #d9a6df;
    --cream: #f4efe2;
    --blush: #f3d8e6;
  }
  * { box-sizing: border-box; margin: 0; padding: 0; }
  html, body { width: 1200px; height: 1200px; overflow: hidden; }
  body {
    background: var(--page-bg);
    font-family: "Roboto Condensed", "Arial Narrow", sans-serif;
    color: var(--ink);
    position: relative;
  }
  .postcard {
    position: absolute;
    left: 249px;
    width: 703px;
    height: 494px;
    overflow: hidden;
  }
  .postcard--front { top: 52px; }
  .postcard--back { top: 658px; }

  .postcard__pattern { position: absolute; inset: 0; }
  .postcard--front .postcard__pattern {
    background:
      radial-gradient(ellipse 260px 200px at 8% 82%, var(--magenta), transparent 75%),
      radial-gradient(ellipse 240px 190px at 88% 40%, var(--hot-pink), transparent 72%),
      radial-gradient(ellipse 220px 120px at 35% 55%, var(--rose), transparent 75%),
      radial-gradient(ellipse 300px 110px at 55% 40%, #e7b9cf, transparent 80%),
      radial-gradient(ellipse 160px 120px at 98% 8%, #f0a6c4, transparent 75%),
      linear-gradient(160deg, #e9dfe3 0%, var(--cream) 60%, #f1ead7 100%);
  }
  .postcard--back .postcard__pattern {
    background:
      radial-gradient(ellipse 320px 260px at 5% 90%, var(--lavender), transparent 75%),
      radial-gradient(ellipse 260px 200px at 95% 35%, #f0b8da, transparent 75%),
      radial-gradient(ellipse 200px 150px at 40% 40%, var(--blush), transparent 80%),
      linear-gradient(150deg, #f1cfe6 0%, #f7ece8 55%, var(--cream) 100%);
  }

  .postcard__frame {
    position: absolute;
    left: 19px; top: 19px; right: 17px; bottom: 19px;
    border: 4px solid var(--frame);
  }

  .brand-mark {
    position: absolute;
    left: 287px; top: 180px;
    width: 132px; height: 132px;
    border-radius: 50%;
    background: var(--logo-disc);
    display: flex; align-items: center; justify-content: center;
    text-align: center;
  }
  .brand-mark__name {
    font-family: "Montserrat", sans-serif;
    font-weight: 500;
    font-size: 13px;
    letter-spacing: 0.12em;
    line-height: 1.35;
    color: var(--white);
    text-transform: uppercase;
  }

  .back-copy { position: absolute; inset: 0; }
  .back-copy__title {
    position: absolute; left: 30px; right: 28px; top: 71px;
    text-align: center; white-space: nowrap;
    font-size: 18.5px; letter-spacing: -0.01em;
    font-weight: 400; color: var(--ink);
  }
  .back-copy__intro {
    position: absolute; left: 30px; right: 28px; top: 106px;
    text-align: center; font-size: 15px; line-height: 20px; color: var(--ink-soft);
  }
  .back-copy__heading {
    position: absolute; left: 0; right: 0; top: 169px;
    text-align: center; font-size: 21px; font-weight: 400; color: var(--ink);
  }
  .back-copy__services {
    position: absolute; left: 41px; width: 624px; top: 214px;
    font-size: 15px; line-height: 20px; color: var(--ink-soft);
  }
  .back-copy__services p { text-indent: 18px; text-align: justify; }
  .back-copy strong { font-weight: 700; color: var(--ink); }
  .back-copy__cta {
    position: absolute; left: 0; right: 0; top: 337px;
    text-align: center; font-size: 16px; line-height: 22px; color: var(--ink);
  }

  .contact-row {
    position: absolute; left: 90px; right: 84px; top: 406px;
    display: flex; justify-content: space-between; align-items: center;
  }
  .contact-item { display: flex; align-items: center; gap: 6px; }
  .contact-item__circle {
    width: 48px; height: 48px; border-radius: 50%;
    border: 3px solid var(--ink);
  }
  .contact-item__icon { width: 48px; height: 48px; }
  .contact-item__text {
    font-size: 33px; font-weight: 700; letter-spacing: -0.02em; color: var(--ink);
  }
</style>
</head>
<body>

  <section class="postcard postcard--front">
    <div class="postcard__pattern" role="img" aria-label="Low-poly geometric pattern in magenta, pink and cream facets"></div>
    <div class="postcard__frame"></div>
    <div class="brand-mark">
      <span class="brand-mark__name">Kestrel<br>Interiors</span>
    </div>
  </section>

  <section class="postcard postcard--back">
    <div class="postcard__pattern" role="img" aria-label="Soft low-poly geometric pattern in lavender, pink and cream facets"></div>
    <div class="postcard__frame"></div>

    <div class="back-copy">
      <h1 class="back-copy__title">Marlie from Kestrel Interiors is partnering up with Bellora and Gwenda from Pim Locks</h1>
      <p class="back-copy__intro">
        As we have something special in common, we both want our clients to <strong>look &amp; feel fabulous.</strong><br>
        <strong>Marlie</strong> is offering the loyal clients of <strong>Pim Locks</strong> a special in <strong>home consult at a reduced rate.</strong>
      </p>
      <h2 class="back-copy__heading">what we do:</h2>
      <div class="back-copy__services">
        <p><strong>We create innovative yet practical design solutions, window treatments &amp; furniture, which are stylish, happy &amp; memorable.</strong> Design to us is about <strong>you</strong>, who you are &amp; how you live, we are passionate about creating a space that is for you and about you.</p>
        <p>A well-designed space makes you feel 10 years younger and truly fabulous to be in, it does not have to cost the earth, but it is something everyone should go home to…</p>
      </div>
      <p class="back-copy__cta">Contact us to find out how we can add value<br>and create a space that makes you feel wonderful to be in.</p>

      <div class="contact-row">
        <div class="contact-item">
          <span class="contact-item__circle"></span>
          <span class="contact-item__text">kestrel interiors</span>
        </div>
        <div class="contact-item">
          <svg class="contact-item__icon" viewBox="0 0 48 48" aria-hidden="true">
            <circle cx="24" cy="24" r="21.5" fill="none" stroke="#2e2a2b" stroke-width="3"/>
            <path d="M16 13.5c1-1 2.3-1 3 .2l2.4 3.8c.6 1 .4 2-.4 2.7l-1.6 1.4c1.2 2.8 3.6 5.3 6.5 6.6l1.4-1.6c.7-.8 1.8-1 2.7-.4l3.8 2.4c1.2.7 1.2 2 .2 3l-1.8 1.8c-1.6 1.6-4.3 1.7-7 .4-5.1-2.5-9.2-6.6-11.7-11.7-1.3-2.7-1.2-5.4.4-7z" fill="none" stroke="#2e2a2b" stroke-width="2.4" stroke-linejoin="round"/>
            <path d="M27 13.5a8 8 0 0 1 7.5 7.5M27 9.5a12 12 0 0 1 11.5 11.5" fill="none" stroke="#2e2a2b" stroke-width="2.2" stroke-linecap="round"/>
          </svg>
          <span class="contact-item__text">0413 925 716</span>
        </div>
      </div>
    </div>
  </section>

</body>
</html>
```